Looking for potential sellers

We help people buy and sell homes and are currently looking for potential home sellers. We offer low commissions, are the Local Colorado Springs and Falcon Experts, homes selling fast and at top dollar, Free expert pricing opinions and Consultations, over 9 years of experience, top rated Realtors creative and aggressive marketing strategies. Don't just tour the town, ROAM Kestrelby. phone number 555-013-8842 web roamkestrelby.example

```html
<!DOCTYPE html>
<html lang="en">
<head>
<meta charset="utf-8">
<title>Harrowmere Postcard – Seller Outreach</title>
<link href="https://fonts.googleapis.com/css2?family=Barlow+Semi+Condensed:wght@600;700;800&display=swap" rel="stylesheet">
<style>
  :root {
    --stage: #1b1b1d;
    --taupe: #9a8676;
    --taupe-light: #a8968a;
    --taupe-dark: #8a7667;
    --band: #b3a397;
    --olive: #8f9a2e;
    --white: #ffffff;
    --rule: #e9e2dc;
    --stamp: #d1d2d4;
    --address-line: #bdbdbd;
  }
  * { margin: 0; padding: 0; box-sizing: border-box; }
  html, body { width: 1002px; height: 1200px; overflow: hidden; background: var(--stage); }
  body { position: relative; font-family: "Barlow Semi Condensed", "Arial Narrow", sans-serif; color: var(--white); }

  .card {
    position: absolute; left: 122px; width: 757px; height: 504px; overflow: hidden;
    background: radial-gradient(ellipse at 40% 45%, var(--taupe-light), var(--taupe) 55%, var(--taupe-dark));
  }
  .card--front { top: 84px; }
  .card--back { top: 612px; }

  .text { position: absolute; font-weight: 700; text-transform: uppercase; line-height: 1; white-space: nowrap; text-shadow: 0 1px 2px rgba(60,45,35,.35); }

  .headline-band {
    position: absolute; left: 0; top: 0; width: 100%; height: 130px;
    background: linear-gradient(var(--band), #a59386);
    border-bottom: 1px solid rgba(255,255,255,.12);
  }
  .headline { position: absolute; top: 26px; width: 100%; text-align: center; font-size: 46px; font-weight: 800; line-height: 50px; letter-spacing: -.3px; text-transform: uppercase; text-shadow: 0 1px 3px rgba(60,45,35,.35); }

  .rule { position: absolute; left: 32px; height: 2px; background: var(--rule); }

  .agent-photo {
    position: absolute; left: 486px; top: 140px; width: 271px; height: 364px;
    background: linear-gradient(160deg, #c9997a 0%, #b27f62 40%, #5d5a5e 75%, #3d3b3f 100%);
    border-top-left-radius: 120px;
  }

  .brand { position: absolute; display: flex; align-items: center; gap: 8px; font-weight: 700; color: var(--white); }
  .brand__mark { background: var(--olive); display: inline-block; }
  .brand__name { text-transform: uppercase; line-height: 1; }

  .stripe { position: absolute; left: 0; top: 0; }
  .stamp { position: absolute; left: 627px; top: 45px; width: 95px; height: 93px; background: var(--stamp); }
  .address-line { position: absolute; left: 430px; width: 292px; height: 2px; background: var(--address-line); }
</style>
</head>
<body>

<section class="card card--front">
  <div class="headline-band"></div>
  <h1 class="headline">Don't just tour the town,<br>ROAM Kestrelby.</h1>

  <div class="agent-photo" role="img" aria-label="Portrait photo of the agent in a dark blazer and light blue shirt"></div>

  <p class="text" style="left:35px;top:172px;font-size:27px;">We help people</p>
  <p class="text" style="left:35px;top:204px;font-size:42px;font-weight:800;">Buy and sell homes</p>
  <p class="text" style="left:35px;top:248px;font-size:14px;">And are currently looking for potential home sellers</p>
  <div class="rule" style="top:274px;width:415px;"></div>

  <p class="text" style="left:35px;top:289px;font-size:27px;">We offer low commissions</p>
  <p class="text" style="left:35px;top:322px;font-size:15.5px;">Local Colorado Springs and Falcon experts,</p>
  <p class="text" style="left:35px;top:342px;font-size:15.5px;">Homes selling fast and at top dollar</p>
  <div class="rule" style="top:369px;width:370px;"></div>

  <p class="text" style="left:34px;top:386px;font-size:52px;font-weight:800;">555-013-8842</p>
  <p class="text" style="left:35px;top:436px;font-size:27px;text-transform:none;">ROAMKESTRELBY.EXAMPLE</p>

  <div class="brand" style="left:372px;top:412px;">
    <span class="brand__mark" style="width:14px;height:14px;"></span>
    <span class="brand__name" style="font-size:22px;">Harrowmere</span>
  </div>
</section>

<section class="card card--back">
  <svg class="stripe" width="757" height="504" viewBox="0 0 757 504" aria-hidden="true">
    <polygon points="484,0 757,0 757,504 382,504" fill="var(--white)"/>
    <polygon points="470,0 484,0 382,504 368,504" fill="var(--olive)"/>
    <polygon points="0,94 457,94 448,136 0,136" fill="var(--white)"/>
  </svg>

  <p class="text" style="left:38px;top:36px;font-size:21px;">Free expert pricing</p>
  <p class="text" style="left:38px;top:64px;font-size:21px;">Opinions and consultations</p>
  <p class="text" style="left:38px;top:104px;font-size:23px;color:var(--olive);text-shadow:none;">Over 9 years of experience</p>
  <p class="text" style="left:38px;top:150px;font-size:21px;">Top rated realtors creative and</p>
  <p class="text" style="left:38px;top:178px;font-size:21px;">Aggressive marketing strategies.</p>

  <div class="brand" style="left:56px;top:286px;gap:12px;">
    <span class="brand__mark" style="width:26px;height:26px;"></span>
    <span class="brand__name" style="font-size:44px;">Harrowmere</span>
  </div>

  <p class="text" style="left:45px;top:384px;font-size:52px;font-weight:800;">555-013-8842</p>
  <p class="text" style="left:46px;top:436px;font-size:27px;">ROAMKESTRELBY.EXAMPLE</p>

  <div class="stamp"></div>
  <div class="address-line" style="top:342px;"></div>
  <div class="address-line" style="top:390px;"></div>
  <div class="address-line" style="top:438px;"></div>
</section>

</body>
</html>
```